Ad design for a macarons brand

We are a dessert brand with one product line: macarons. Our products delight. Every bite is a dream!

We are launching a new product and would like to lunch a small tactical campaign for the product to boost sales.

The new macron is mango ganache and the middle a mix of sour mango and yuzu (https://www.plumvarell.com/about-the-fruit-584302).

Here are some images we took of the new macaron
https://www.fennlocker.com/sh/qrtwpzhkvbmls/AAFJtRWD-nxPlkhQZ7CeW4DLp?dl=0

I attach the brand guideline document.

Required sizes

1080 x 1350
1080 x 1920

```html
<!DOCTYPE html>
<html lang="en">
<head>
<meta charset="utf-8">
<title>Mirau – Every Bite's a Dream</title>
<link rel="stylesheet" href="https://fonts.googleapis.com/css2?family=Playfair+Display:wght@400&display=swap">
<style>
  :root {
    --teal: #00c4d6;
    --teal-light: #3ed8de;
    --white: #ffffff;
    --pink: #f7919f;
    --yellow: #fdd046;
    --grey: #dcdcdc;
  }
  * { margin: 0; padding: 0; box-sizing: border-box; }
  html, body { width: 960px; height: 1200px; overflow: hidden; background: var(--teal); }
  .ad {
    position: relative;
    width: 960px;
    height: 1200px;
    overflow: hidden;
    background: var(--teal);
    font-family: "Playfair Display", serif;
    color: var(--white);
  }
  .ad__art { position: absolute; inset: 0; width: 960px; height: 1200px; }
  .brand-name {
    position: absolute;
    top: 52px;
    right: 40px;
    width: 280px;
    text-align: center;
    font-size: 76px;
    font-weight: 400;
    line-height: 1;
    letter-spacing: 2px;
  }
  .headline {
    position: absolute;
    top: 196px;
    left: 0;
    width: 960px;
    text-align: center;
    font-size: 86px;
    font-weight: 400;
    line-height: 86px;
  }
</style>
</head>
<body>
<main class="ad">
  <svg class="ad__art" viewBox="0 0 1080 1350">
    <defs>
      <clipPath id="photo-clip"><circle cx="790" cy="1110" r="500"/></clipPath>
      <radialGradient id="macaron-tones" cx="0.45" cy="0.5" r="0.6">
        <stop offset="0" stop-color="#f5b447"/>
        <stop offset="0.6" stop-color="#ee9f38"/>
        <stop offset="1" stop-color="#e3d9cc"/>
      </radialGradient>
    </defs>

    <g class="swoosh" fill="none" stroke="var(--teal-light)" stroke-width="70" stroke-linecap="round">
      <path d="M270 -20 C 200 90, 40 160, 35 330 C 30 470, 150 540, 235 580"/>
      <path d="M820 -20 C 840 120, 850 260, 790 360 C 730 450, 620 480, 520 485"/>
    </g>

    <circle class="dot dot--pink" cx="355" cy="500" r="62" fill="var(--pink)"/>
    <circle class="ring ring--yellow" cx="422" cy="560" r="58" fill="none" stroke="var(--yellow)" stroke-width="14"/>
    <circle class="dot dot--pink" cx="203" cy="798" r="50" fill="var(--pink)"/>

    <g class="social" fill="none" stroke="var(--white)" stroke-width="5">
      <circle cx="53" cy="686" r="28"/>
      <circle cx="140" cy="686" r="28"/>
      <circle cx="228" cy="686" r="28"/>
      <circle cx="315" cy="686" r="28"/>
    </g>

    <path class="blob blob--yellow" d="M0 860 C 40 900, 70 960, 62 1000 C 55 1035, 25 1045, 0 1040 Z" fill="var(--yellow)"/>
    <path class="hook" d="M-10 815 C 120 850, 200 960, 200 1090 C 200 1180, 140 1270, 100 1275 C 60 1280, 45 1230, 72 1190 C 112 1120, 122 1040, 92 970 C 62 910, 25 882, -10 872" fill="none" stroke="var(--white)" stroke-width="18" stroke-linejoin="round"/>

    <circle class="frame" cx="790" cy="1110" r="565" fill="var(--grey)"/>
    <g class="product-photo" role="img" aria-label="Photo of mango and yuzu macarons on white baking paper" clip-path="url(#photo-clip)">
      <rect x="280" y="600" width="1020" height="1020" fill="url(#macaron-tones)"/>
    </g>
  </svg>

  <div class="brand-name">MIRAU</div>

  <h1 class="headline">EVERY BITE’S A<br>DREAM</h1>
</main>
</body>
</html>
```